Tradeon Cup Championship Webdesign project

We need a webdesign for the project called Tradeon. Tradeon™ is an international Forex trading competition to see who can make the most profit in two weeks with all players getting an equal starting sum. Participation is free with no strings attached and the prize money is real, with a total prize pool of $50,000! At the moment Tradeon vol. 2 is about to get launched and we would like to have a new design. On the new website traders should be able to create their own competitions, as well as to invite each other for the cometition.
Updates

Requirements
Must have
• http://www.tradeoncup-example.com/ please refer to this website for the further details.

The website should also include the competition section where traders can invite each other for the competition. It should work similarly to poker competitions.

```html
<!DOCTYPE html>
<html lang="en">
<head>
<meta charset="utf-8">
<title>Tradeon Cup Championship</title>
<link rel="stylesheet" href="https://fonts.googleapis.com/css2?family=Arimo:wght@400;700&family=Marcellus&family=PT+Sans+Narrow:wght@400;700&display=swap">
<style>
:root{
  --page:#f6f6f6;
  --sky-top:#93c4ec;
  --sky-mid:#5d9ad6;
  --sky-bottom:#2468b2;
  --white:#ffffff;
  --panel:#f2f4f6;
  --stripe:#e9ebee;
  --ink:#3b3b3b;
  --muted:#6a6a6a;
  --link:#2f6fb0;
  --heading:#4a86c0;
  --nav-ink:#555;
  --btn:#1f6aa8;
  --btn-dark:#17548a;
  --gold:#d7b23a;
  --gold-light:#f4dc7a;
}
*{box-sizing:border-box;margin:0;padding:0}
html,body{width:1037px;height:1200px;overflow:hidden;background:var(--page);font-family:"Arimo",Arial,sans-serif;color:var(--ink)}
.site{position:absolute;left:17px;top:29px;width:1005px;height:1140px;background:linear-gradient(180deg,var(--sky-top) 0%,var(--sky-mid) 45%,var(--sky-bottom) 100%)}
.abs{position:absolute}
.brand{left:60px;top:40px;display:flex;align-items:center;gap:20px}
.brand-dot{width:92px;height:92px;border-radius:50%;background:var(--gold)}
.brand-name{font-family:"Marcellus",serif;font-size:52px;color:var(--white);letter-spacing:1px}
.countdown-label{left:674px;top:14px;font-family:"PT Sans Narrow",sans-serif;font-size:15px;color:var(--btn-dark)}
.countdown-label span{font-family:"Arimo",sans-serif;font-size:11px;color:var(--link)}
.count-box{top:42px;width:58px;height:48px;background:var(--white);box-shadow:0 1px 3px rgba(0,0,0,.2);text-align:center;color:var(--link)}
.count-box b{display:block;font-weight:400;font-size:19px;margin-top:8px}
.count-box small{font-size:7px;text-transform:uppercase}
.flag{left:659px;top:109px;width:26px;height:26px;border-radius:50%;background:#b43a3a;border:3px solid var(--white)}
.lang{left:691px;top:112px;width:156px;height:18px;border-radius:9px;background:linear-gradient(#fff,#ddd);font-size:10px;color:#555;padding:3px 12px}
.lang i{position:absolute;right:0;top:0;width:16px;height:18px;background:var(--heading);border-radius:0 9px 9px 0}
.account{left:741px;top:138px;font-size:11px;color:var(--btn-dark)}
.participants{left:860px;top:111px;width:99px;height:47px;background:var(--white);text-align:center;box-shadow:0 1px 3px rgba(0,0,0,.2)}
.participants b{display:block;font-weight:400;font-size:27px;color:var(--btn-dark);line-height:30px;margin-top:2px}
.participants small{font-size:7px;color:var(--muted);text-transform:uppercase}
.nav{left:289px;top:190px;width:668px;height:36px;border-radius:6px;background:linear-gradient(#fff,#e6e6e6);box-shadow:0 1px 3px rgba(0,0,0,.25);display:flex;align-items:center;justify-content:space-around;padding:0 8px}
.nav a{font-family:"PT Sans Narrow",sans-serif;font-size:16px;color:var(--nav-ink);text-decoration:none;letter-spacing:.5px}
.hero{left:53px;top:257px;width:614px;height:256px;border-radius:8px;overflow:hidden;background:linear-gradient(180deg,#1c1c1c 0%,#5a6156 55%,#8e9488 100%)}
.hero h1{position:absolute;left:32px;top:24px;font-family:"PT Sans Narrow",sans-serif;font-size:27px;color:var(--white);font-weight:700}
.hero p{position:absolute;left:32px;top:55px;width:560px;font-family:"PT Sans Narrow",sans-serif;font-size:23px;color:#bcd8f2;text-align:center;line-height:24px}
.btn{position:absolute;background:linear-gradient(var(--btn),var(--btn-dark));color:var(--white);font-size:12px;text-align:center;border-radius:3px;box-shadow:0 1px 3px rgba(0,0,0,.4)}
.prize{left:697px;top:257px;width:260px;height:256px;border-radius:8px;background:radial-gradient(circle at 60% 35%,#3f97e4,#0d4f9c 75%);color:var(--white);text-align:center}
.prize h2{font-family:"PT Sans Narrow",sans-serif;font-size:25px;margin-top:36px;line-height:24px}
.prize h2 span{display:block;font-family:"Arimo",sans-serif;font-size:50px;line-height:54px}
.prize p{font-size:11px;font-weight:700;line-height:15px;margin-top:8px}
.pager{top:522px;width:24px;height:24px;border-radius:50%;background:linear-gradient(#fff,#ddd);font-size:10px;color:#888;text-align:center;line-height:24px}
.tab{top:554px;height:35px;border-radius:6px 6px 0 0;background:linear-gradient(#fff,#e8e8e8);font-family:"PT Sans Narrow",sans-serif;font-size:15px;color:var(--nav-ink);padding:10px 15px}
.tab.active{background:var(--panel);height:40px}
.board{left:53px;top:588px;width:614px;height:303px;background:var(--panel);border-radius:0 6px 6px 6px}
.board table{position:absolute;left:18px;top:30px;width:575px;border-collapse:collapse;font-size:11px}
.board th{font-family:"PT Sans Narrow",sans-serif;font-size:17px;color:var(--heading);text-align:left;height:44px;font-weight:700}
.board td{height:31px}
.board tr:nth-child(even) td{background:var(--stripe)}
.board td:first-child,.board th:first-child{padding-left:37px}
.board th:first-child{padding-left:37px}
.regions{position:absolute;left:47px;top:230px;font-size:11px;color:var(--link);line-height:18px}
.regions .more{padding-left:0}
.gold{left:53px;top:920px;width:614px;height:111px;border-radius:8px;background:linear-gradient(90deg,#b88a1c 0%,var(--gold) 30%,var(--gold-light) 70%,#e3c25a 100%)}
.gold h3{position:absolute;left:199px;top:32px;font-weight:400;font-size:23px;color:#3d3315}
.gold p{position:absolute;left:199px;top:62px;font-size:12px;color:#5a4a1a}
.news-tab{left:696px;top:554px;width:60px;height:40px;border-radius:6px 6px 0 0;background:var(--panel);font-family:"PT Sans Narrow",sans-serif;font-size:15px;color:var(--nav-ink);padding:10px 12px}
.news-more{left:772px;top:566px;font-size:11px;color:var(--white)}
.news{left:696px;top:588px;width:262px;height:474px;background:var(--panel);border-radius:0 6px 6px 6px}
.news-item{position:absolute;left:20px;width:235px}
.thumb{position:absolute;left:0;top:0;width:68px;height:59px;background:linear-gradient(135deg,#7a8a3a,#c9a43a);border:2px solid var(--white)}
.thumb.dark{background:radial-gradient(circle,#c58a2a,#2a2418)}
.news-item h4{margin-left:83px;font-family:"PT Sans Narrow",sans-serif;font-size:17px;color:var(--heading);line-height:18px}
.news-item time{display:block;margin-left:83px;font-size:10px;font-weight:700;color:#555;margin-top:2px}
.news-item p{margin-left:83px;font-size:10px;color:#555;line-height:17px}
.news-item p a{color:var(--link);text-decoration:none}
.connect{left:708px;top:1082px;display:flex;align-items:center;gap:8px;font-family:"PT Sans Narrow",sans-serif;font-size:17px;color:var(--white);font-weight:700}
.connect span{display:block;width:26px;height:26px;border-radius:50%;background:var(--white)}
.connect span:first-child{margin-left:6px}
.footer-links{left:57px;top:1110px;font-size:10px;color:var(--white)}
.copyright{left:731px;top:1110px;font-size:10px;color:#cfe0f2}
</style>
</head>
<body>
<div class="site">
  <div class="abs brand"><div class="brand-dot"></div><div class="brand-name">Tradeon™</div></div>

  <div class="abs countdown-label">COUNTDOWN <span>- Check Schedules</span></div>
  <div class="abs count-box" style="left:677px"><b>34</b><small>Days</small></div>
  <div class="abs count-box" style="left:750px"><b>11</b><small>Hours</small></div>
  <div class="abs count-box" style="left:826px"><b>52</b><small>Minutes</small></div>
  <div class="abs count-box" style="left:900px"><b>07</b><small>Seconds</small></div>

  <div class="abs flag"></div>
  <div class="abs lang">Select your language<i></i></div>
  <div class="abs account">Register &nbsp;|&nbsp; Login</div>
  <div class="abs participants"><b>958</b><small>Round participants</small></div>

  <nav class="abs nav">
    <a>ABOUT</a><a>NEWS</a><a>STANDING</a><a>SCHEDULE</a><a>FAQs</a><a>BROKERS</a><a>DOWNLOAD</a>
  </nav>

  <section class="abs hero" role="img" aria-label="Close-up photograph of a banknote">
    <h1>TRADEON™ IS AN INTERNATIONAL TRADING COMPETITION</h1>
    <p>See who can make the most profit in two weeks with all players getting an equal starting sum.</p>
    <div class="btn" style="left:497px;top:201px;width:88px;height:33px;line-height:33px">JOIN NOW!</div>
  </section>

  <section class="abs prize">
    <h2>PRIZE FUND OF<span>$50,000</span></h2>
    <p>Participation is free, no strings<br>attached. Create &amp; invite.</p>
    <div class="btn" style="left:62px;top:182px;width:142px;height:36px;line-height:36px;font-family:'PT Sans Narrow',sans-serif;font-size:17px;font-weight:700">ENTER TODAY</div>
  </section>

  <div class="abs pager" style="left:620px">&laquo;</div>
  <div class="abs pager" style="left:648px">&raquo;</div>
  <div class="abs pager" style="left:913px">&laquo;</div>
  <div class="abs pager" style="left:942px">&raquo;</div>

  <div class="abs tab active" style="left:53px;width:166px">CURRENT TOURNAMENTS</div>
  <div class="abs tab" style="left:221px;width:166px">ENDED TOURNAMENTS</div>
  <div class="abs tab" style="left:389px;width:166px">PLAYER RATING</div>

  <section class="abs board">
    <table>
      <tr><th>NICKNAME</th><th>COUNTRY</th><th>PROFIT</th></tr>
      <tr><td>1. Hosebarena</td><td>United Kingdom</td><td>36 502</td></tr>
      <tr><td>2. Sorcere</td><td>Estonia</td><td>25 461</td></tr>
      <tr><td>3. Angelbuffy</td><td>Latvia</td><td>19 872</td></tr>
      <tr><td>4. Sirob</td><td>Latvia</td><td>17 903</td></tr>
      <tr><td>5. Uriuk</td><td>Lithuania</td><td>15 750</td></tr>
    </table>
    <div class="regions">
      <div style="padding-left:0">&raquo; View more events</div>
      Russia &amp; CIS &nbsp;| &nbsp;Eastern Europe &nbsp;| Westerb &amp; Northern Europe &nbsp;| &nbsp;Ibero-America<br>
      East &amp; Southeast Asia &nbsp;| &nbsp;Rest of the world
    </div>
    <div class="btn" style="left:463px;top:247px;width:128px;height:34px;line-height:34px">CREATE YOUR OWN</div>
  </section>

  <section class="abs gold" role="img" aria-label="Stacked gold bars on a golden background">
    <h3>Gold Accounts</h3>
    <p>Your private Gold Reserve!</p>
  </section>

  <div class="abs news-tab">NEWS</div>
  <div class="abs news-more">More news</div>
  <section class="abs news">
    <article class="news-item" style="top:66px">
      <div class="thumb" role="img" aria-label="Competition trophy thumbnail"></div>
      <h4>3RD BASIC TRADEON</h4><time>August 03, 2011</time>
      <p>We are pleased to announce that registration for the 3rd Tradeon™ . <a>Read More...</a></p>
    </article>
    <article class="news-item" style="top:172px">
      <div class="thumb dark" role="img" aria-label="Winners trophy thumbnail"></div>
      <h4>WINNERS!</h4><time>June 20, 2011</time>
      <p>Winners and prizes of the Special Round of the Serbia and Croatia. <a>Read More...</a></p>
    </article>
    <article class="news-item" style="top:276px">
      <div class="thumb" role="img" aria-label="Competition trophy thumbnail"></div>
      <h4>3RD BASIC TRADEON</h4><time>August 03, 2011</time>
      <p>We are pleased to announce that registration for the 3rd Tradeon™ . <a>Read More...</a></p>
    </article>
    <article class="news-item" style="top:380px">
      <div class="thumb dark" role="img" aria-label="Winners trophy thumbnail"></div>
      <h4>WINNERS!</h4><time>June 20, 2011</time>
      <p>Winners and prizes of the Special Round of the Serbia and Croatia. <a>Read More...</a></p>
    </article>
  </section>

  <div class="abs connect">Connect with us! <span></span><span></span><span></span><span></span></div>
  <div class="abs footer-links">Live Chat &nbsp;| &nbsp;Terms and Conditions &nbsp;| &nbsp;Contact Us</div>
  <div class="abs copyright">© 2009 TRADEON &nbsp;| &nbsp;ALL RIGHTS RESERVED</div>
</div>
</body>
</html>
```